The Lantern Guide

I am a life coach specializing in helping people with depression and bipolar disorder. I would like a nice, fun design for a business card.

```html
<!DOCTYPE html>
<html lang="en">
<head>
<meta charset="utf-8">
<title>The Lantern Guide — Business Card</title>
<link rel="stylesheet" href="https://fonts.googleapis.com/css2?family=Open+Sans:wght@400&family=Raleway:wght@400&display=swap">
<style>
  :root {
    --page: #ffffff;
    --card-white: #ffffff;
    --navy: #2e3192;
    --sky: #29abe2;
    --ocean: #1b75bc;
    --frame: #1f7aa8;
    --wave: #1a7fb0;
    --glow: #ff0000;
    --ink-light: #ffffff;
  }
  * { margin: 0; padding: 0; box-sizing: border-box; }
  html, body {
    width: 1200px; height: 1200px; overflow: hidden;
    background: var(--page);
  }
  .business-card {
    position: absolute;
    left: 229px; top: 371px;
    width: 747px; height: 428px;
    background: var(--card-white);
    border: 2px solid var(--frame);
    overflow: hidden;
  }
  .contact-band {
    position: absolute;
    left: 0; right: 0; top: 213px; bottom: 0;
    background: var(--navy);
  }
  .accent-column {
    position: absolute;
    left: 86px; top: 0;
    width: 129px; height: 371px;
    background: var(--sky);
  }
  .accent-dot {
    position: absolute;
    left: 122px; top: 282px;
    width: 56px; height: 56px;
    border-radius: 50%;
    background: var(--glow);
  }
  .identity {
    position: absolute;
    left: 331px; top: 50px;
    display: inline-block;
    font-family: "Open Sans", sans-serif;
  }
  .identity-name {
    font-size: 45px; font-weight: 400; line-height: 1;
    letter-spacing: -0.5px; white-space: nowrap;
    color: var(--navy);
  }
  .identity-name .accent-word { color: var(--ocean); }
  .identity-role {
    position: relative;
    height: 34px; margin-top: -2px;
  }
  .wave-line {
    position: absolute; left: 2px; top: 0;
    width: 200px; height: 34px;
  }
  .role-title {
    position: absolute; right: 0; top: 2px;
    font-size: 26px; color: var(--ocean); white-space: nowrap;
  }
  .contact-list {
    position: absolute;
    left: 331px; top: 242px;
    list-style: none;
    font-family: "Raleway", sans-serif;
    font-variant-numeric: lining-nums;
    color: var(--ink-light);
    font-size: 29px;
  }
  .contact-item {
    display: flex; align-items: center;
    height: 42px; margin-bottom: 14px;
    white-space: nowrap;
  }
  .contact-item:nth-child(2) { margin-bottom: 16px; }
  .contact-icon {
    width: 28px; height: 28px; margin-right: 11px; flex: none;
  }
</style>
</head>
<body>
  <div class="business-card">
    <div class="contact-band"></div>
    <div class="accent-column"></div>
    <div class="accent-dot"></div>

    <div class="identity">
      <h1 class="identity-name">The Lantern <span class="accent-word">Guide</span></h1>
      <div class="identity-role">
        <svg class="wave-line" viewBox="0 0 200 34" aria-hidden="true">
          <path d="M0 20 Q10 10 20 20 T40 20 T60 20 L200 20"
            fill="none" stroke="var(--wave)" stroke-width="1.6" stroke-linecap="round"/>
        </svg>
        <p class="role-title">Life Coach</p>
      </div>
    </div>

    <ul class="contact-list">
      <li class="contact-item">
        <svg class="contact-icon" viewBox="0 0 28 28" aria-hidden="true">
          <path d="M6 3 L10 3 L12 9 L9 11 C10.5 15 13 17.5 17 19 L19 16 L25 18 L25 22 C25 24 23 25 21 25 C12 24 4 16 3 7 C3 5 4 3 6 3 Z"
            fill="none" stroke="var(--ink-light)" stroke-width="1.6" stroke-linejoin="round"/>
        </svg>
        <span>+00 555 246 80</span>
      </li>
      <li class="contact-item">
        <svg class="contact-icon" viewBox="0 0 28 28" aria-hidden="true">
          <rect x="2" y="6" width="24" height="16" fill="none" stroke="var(--ink-light)" stroke-width="1.8"/>
          <polyline points="2,6 14,15 26,6" fill="none" stroke="var(--ink-light)" stroke-width="1.8"/>
        </svg>
        <span>hello@lanternguide.com</span>
      </li>
      <li class="contact-item">
        <svg class="contact-icon" viewBox="0 0 28 28" aria-hidden="true">
          <path d="M14 26 C8 18 5 14 5 10 A9 9 0 0 1 23 10 C23 14 20 18 14 26 Z"
            fill="none" stroke="var(--ink-light)" stroke-width="1.6" stroke-linejoin="round"/>
          <circle cx="14" cy="10" r="3.5" fill="none" stroke="var(--ink-light)" stroke-width="1.6"/>
        </svg>
        <span>Harbour Lane 7-3B.</span>
      </li>
    </ul>
  </div>
</body>
</html>
```